Business Card Design for drone videography and photography

I have a Vorkel Skyra 3 drone. I am looking for a logo to somehow incorporate with my business name. I don't even know what is an appropriate font. I am most filming real estate homes. I want something simplistic and a logo that makes sense for the business that I'm in. xxxxxxxxxxxxxxxxxxxxxxxxxxxxxxxxxxxxxxxxxxxxxxxxxxxxxxxxxxxxxxxxxxxxxxxxxxxxxxxxxxxxxxxxxxxxxxxxxxxxxxxxxxxxxxxxxxxxxxxxxxxxxxxxxxxxxxxxxxxxxxxxxxxxxxxxxxxxxxxxxxxxxxxxxxxxxxxxxxxxxxxxxxxxxxxxxxxxxxxxxxxxxxxxxxxxxxxxxxxxxxxxxxxxxxxxxxxxxxxxxxxxxxxxxxxxxxxxxxxxxxxxxxxxxxxxxxxxxxxxxxxxxxxxxxxxxxxxxxxxxxxxxxxxxxxxxxxxxxxxxxxxxxxxxxxxxxxxxxxxxxxxxxxxxxxxxxxxxxxxxxxxxxxxxxxxxxxxxxxxxxxxxxxxxxxxxxxxxxxxxxxxxxxxxxxxxxxxxxxxxxxxxxxxxxxxxxxxxxxxxxxxxxxxxxxxxxxxxxxxxxxxxxxxxxxxxxxxxxxxxxxxxxxxxxxxxxxxxxxxxxxxxxxxxxxxxxxxxxxxxxxxxxxxxxxxxxxxxxxxxxxxxxxxxxxxxxxxxxxxxxxxxxxxxxxxxxxxxxxxxxxxxxxxxxxxxxxxxxxxxxxxxxxxxxxxxxxxxxxxxxxxxxxxxxxxxxxxxxxxxxxxxxxxxxxxxxxxxxxxxxxxxxxxxxxxxxxxxxxxxxxxxxxxxxxxxxxxxxxxxxxxxxxxxxxxxxxxxxxxxxxxxxxxxxxxxxxxxxxxxxxxxxxxxxxxxxxxxxxxxxxxxxxxxxxxxxxxxxxxxxxxxxxxxxxxxxxxxxxxxxxxxxxxxxxxxxxxxxxxxxxxxxxxxxxxxxxxxxxxxxxxxxxxxxxxxxxxxxxxxxxxxxxxxxxxxxxxxxxxxxxxxxxxxxxxxxxxxxxxxxxxxxxxxxxxxxxxxxxxxxxxxxxxxxxxxxxxxxxxxxxxxxxxxxxxxxxxxxxxxxxxxxxxxxxxxxxxxxxxxxxxxxxxxxxxxxxxxxxxxxxxxxxxxxxxxxxxxxxxxxxxxxxxxxxxxxxxxxxx

Target Market(s)

Real estate

Industry/Entity Type

Business

Contact Information for Business Card

TRASK AERIAL IMAGING
Daniel Trask
Owner/Operator

40528 Birchwood Ct.
Port Alden ND 63514

314-555-0187
dtrask@traskaerialimaging.com

NAB Drone Certified
Insured
Section 333 Exempt
Vexo Flight Class Certified

Font styles to use
Other font styles liked:
• PUMP DEMI BOLD LET

Requirements
Must have
• Maybe have the certifications on the back??? The business card must be more serious than playful
Nice to have
• Possibly have the logo work itself into the business name?
Should not have
• nothing that looks like a "fun" business. I want this business card to look professional but also simplistic. I don't want a picture that I took from my drone as the background.

```html
<!DOCTYPE html>
<html lang="en">
<head>
<meta charset="utf-8">
<title>Trask Aerial Imaging — Business Card</title>
<link rel="stylesheet" href="https://fonts.googleapis.com/css2?family=Questrial&display=swap">
<style>
  :root {
    --backdrop: #c4dccf;
    --brand-blue: #2a86f6;
    --card-white: #ffffff;
    --text-white: #ffffff;
    --soft-white: rgba(255,255,255,0.9);
    --card-shadow: rgba(40,70,60,0.18);
  }
  * { margin: 0; padding: 0; box-sizing: border-box; }
  html, body {
    width: 1200px; height: 1000px; overflow: hidden;
    background: var(--backdrop);
    font-family: "Questrial", "Helvetica Neue", Arial, sans-serif;
  }
  .stage { position: relative; width: 1200px; height: 1000px; }

  .card {
    position: absolute; width: 525px; height: 300px;
    border-radius: 32px; overflow: hidden;
    background: var(--card-white);
    box-shadow: 0 10px 30px var(--card-shadow);
  }
  .card--front { left: 50px; top: 210px; }
  .card--back  { left: 625px; top: 210px; }

  .wordmark { text-align: center; color: var(--brand-blue); line-height: 1; }
  .wordmark__name { display: block; font-size: 58px; letter-spacing: 6px; }
  .wordmark__tag  { display: block; font-size: 19px; letter-spacing: 5px; margin-top: 4px; }
  .wordmark--light { color: var(--text-white); }

  /* Front */
  .front__top { height: 158px; display: flex; align-items: center; justify-content: center; padding-top: 14px; }
  .front__band {
    position: absolute; left: 0; right: 0; bottom: 0; height: 142px;
    background: var(--brand-blue); color: var(--text-white);
  }
  .person { position: absolute; left: 96px; top: 12px; }
  .person__name { font-size: 22px; letter-spacing: 2px; }
  .person__role { font-size: 13px; letter-spacing: 2px; color: var(--soft-white); margin-top: 3px; padding-left: 24px; }
  .contact { position: absolute; right: 28px; top: 14px; text-align: right; }
  .contact__phone { font-size: 17px; letter-spacing: 1px; }
  .contact__email { font-size: 11px; margin-top: 6px; color: var(--soft-white); }
  .address { position: absolute; left: 30px; bottom: 22px; font-size: 15px; line-height: 1.35; letter-spacing: 0.5px; font-style: normal; }

  /* Back */
  .back__band {
    height: 140px; background: var(--brand-blue);
    display: flex; align-items: center; justify-content: center; padding-top: 10px;
  }
  .back__band .wordmark__name { font-size: 48px; }
  .back__band .wordmark__tag { font-size: 16px; }
  .credentials {
    list-style: none; text-align: center; color: var(--brand-blue);
    font-size: 16px; line-height: 1.45; padding-top: 26px;
  }

  /* Standalone wordmark */
  .brand-lockup { position: absolute; left: 0; right: 0; top: 640px; }
  .brand-lockup .wordmark__name { font-size: 110px; letter-spacing: 12px; }
  .brand-lockup .wordmark__tag  { font-size: 38px; letter-spacing: 12px; margin-top: 8px; }
</style>
</head>
<body>
<main class="stage">

  <section class="card card--front" aria-label="Card front">
    <div class="front__top">
      <div class="wordmark">
        <span class="wordmark__name">TRASK</span>
        <span class="wordmark__tag">AERIAL IMAGING</span>
      </div>
    </div>
    <div class="front__band">
      <div class="person">
        <div class="person__name">DANIEL TRASK</div>
        <div class="person__role">OWNER/OPERATOR</div>
      </div>
      <div class="contact">
        <div class="contact__phone">555 201 0187</div>
        <div class="contact__email">dtrask@traskaerialimaging.com</div>
      </div>
      <address class="address">
        40528 Birchwood Ct.<br>
        Port Alden ND 63514
      </address>
    </div>
  </section>

  <section class="card card--back" aria-label="Card back">
    <div class="back__band">
      <div class="wordmark wordmark--light">
        <span class="wordmark__name">TRASK</span>
        <span class="wordmark__tag">AERIAL IMAGING</span>
      </div>
    </div>
    <ul class="credentials">
      <li>NAB Drone Certified</li>
      <li>Insured</li>
      <li>Section 333 Exempt</li>
      <li>Vexo Flight Class Certified</li>
    </ul>
  </section>

  <div class="brand-lockup wordmark">
    <span class="wordmark__name">TRASK</span>
    <span class="wordmark__tag">AERIAL IMAGING</span>
  </div>

</main>
</body>
</html>
```